Subscription box needs a bold design for our lock front mailer box

We are a new subscription box service called Petal Crate Box filled with an array of delightful products made by women artisans and business owners. Products include handcrafted bath, beauty and spa products, gourmet delights, home and lifestyle goods, jewelry and accessories. We also place great importance on obtaining organic products from sustainable sources where possible.
Our focus is on lifting women up and on inspiring our customers to do so too. We do this by sourcing all of our products from women, creating a monthly “Kind Spark” card for each box with ideas on how to give another woman a boost, and donating 10% of our proceeds to a woman-focused charity each month. We believe that we will all be stronger if we work together.
We need a bold design for our mailing box that incorporates our logo, our website address, our tag line and possibly our mascot.
The box will be white with red print. We have a template for PDF and EPS from the company we will use to produce the boxes. We are attaching templates, logo, mascot photo, sample pattern and ideas. We would like a designer that can bring their own ideas and we are very open to new thoughts.

Target Market(s)

Women, 25 to 65. Educated with significant disposable income.

Industry/Entity Type

Business

Colors
ec1f27

Requirements
Must have
• A bold look. Must include our logo and tag line "Brighten Someone, Share The Glow"
• Will be red print on a white box.
Nice to have
• Have included file with ideas but am very open to other thoughts and designs.

```html
<!DOCTYPE html>
<html lang="en">
<head>
<meta charset="utf-8">
<title>Petal Crate Box — Mailer Box Panels</title>
<link rel="stylesheet" href="https://fonts.googleapis.com/css2?family=Arimo:wght@700&family=Righteous&display=swap">
<style>
  :root {
    --brand-red: #c8191f;
    --box-white: #e9e9e9;
    --panel-white: #f1f1f1;
    --canvas-bg: #ffffff;
    --edge: #d6d6d6;
  }
  * { box-sizing: border-box; margin: 0; padding: 0; }
  html, body { width: 1200px; height: 1200px; overflow: hidden; background: var(--canvas-bg); }
  .canvas { position: relative; width: 1200px; height: 1200px; }

  .lid-panel {
    position: absolute; left: 90px; top: 150px; width: 720px; height: 460px;
    border: 1px solid var(--edge);
  }
  .lid-pattern {
    position: absolute; inset: 0;
    background: var(--brand-red);
  }
  .lid-label {
    position: absolute; left: 110px; top: 80px; width: 500px; height: 300px;
    background: var(--panel-white); border-radius: 28px;
    display: flex; align-items: center; justify-content: center;
  }
  .brand-name {
    font-family: "Arimo", Arial, sans-serif; font-weight: 700;
    font-size: 50px; letter-spacing: 1px; color: var(--brand-red);
    text-transform: uppercase;
  }

  .side-panel {
    position: absolute; left: 90px; top: 610px; width: 720px; height: 250px;
    background: var(--box-white); border: 1px solid var(--edge); border-top: none;
    display: flex; align-items: center; justify-content: center;
  }
  .tagline {
    font-family: "Righteous", "Trebuchet MS", sans-serif;
    font-size: 40px; color: var(--brand-red);
  }

  .end-panel {
    position: absolute; left: 810px; top: 150px; width: 300px; height: 460px;
    background: var(--brand-red); padding: 60px 28px;
    display: flex; align-items: center;
  }
  .end-copy {
    font-family: "Arimo", Arial, sans-serif; font-weight: 700;
    font-size: 17px; line-height: 1.32; color: #ffffff;
    text-align: justify;
  }
  .end-copy p { text-indent: 1.6em; }
</style>
</head>
<body>
<main class="canvas">
  <section class="lid-panel">
    <div class="lid-pattern" role="img" aria-label="Red lattice pattern of white circles framing the lid"></div>
    <div class="lid-label">
      <span class="brand-name">Petal Crate Box</span>
    </div>
  </section>

  <section class="end-panel">
    <div class="end-copy">
      <p>Lorem ipsum dolor sit amet, curabitur sollicitudin massa nec. Semper aliquam curabitur et, sodales vitae, donec montes parturient consectetuer elit vulputate, orci donec lorem laoreet wisi accumsan lorem.</p>
      <p>Erat turpis, risus posuere tortor id lorem sed nulla. Nascetur laoreet lectus, imperdiet quis consectetuer lacus maecenas mauris.</p>
      <p>Etiam sed leo varius, vulputate arcu amet a, nunc non amet erat in nec dictum.</p>
    </div>
  </section>

  <section class="side-panel">
    <p class="tagline">Brighten Someone, Share The Glow</p>
  </section>
</main>
</body>
</html>
```